Online trading school - Website design

We are building an online trading school (trading of shares, commodities, indices, currencies). The purpose is to teach online traders how to trade successfully. We need to design the homepage of the website and logo (bramwelloq.com will be the domain). The homepage will contain the following elements

- logo
- Sign in and Register links/buttons
- upper menu
- short introduction
- a couple of bullet points 'Why to join our school?'
- sign up form
- text
- bottom menu

Attached is a draft for the designer. The draft is just for an inspiration, the actual structure of the website can be different if the designer thinks so.

The designer is free to choose colors.

School

3 page

```html
<!DOCTYPE html>
<html lang="en">
<head>
<meta charset="utf-8">
<title>Bramwelloq – Online Trading School</title>
<link href="https://fonts.googleapis.com/css2?family=Roboto:wght@300;400;500&display=swap" rel="stylesheet">
<style>
:root{
  --dark:#1e1e1e;
  --blue:#1fa6e8;
  --orange:#ff8c00;
  --ink:#2b2b2b;
  --muted:#555;
  --field:#e6e6e6;
  --panel:#f2f2f2;
  --white:#fff;
}
*{margin:0;padding:0;box-sizing:border-box}
html,body{width:1125px;height:1200px;overflow:hidden}
body{font-family:'Roboto',sans-serif;color:var(--ink);background:var(--white);position:relative}
.abs{position:absolute}
.topbar{left:0;top:0;width:1125px;height:36px;background:var(--dark)}
.social{top:6px;width:24px;height:24px}
.social.one{left:83px;background:#3b5998}
.social.two{left:113px;background:#29b6f0}
.social.three{left:143px;background:#dd2c22}
.account{top:11px;font-size:12px;color:var(--white)}
.account .signin{color:var(--blue)}
.account .sep{margin:0 14px 0 20px}
.header{left:0;top:36px;width:1125px;height:68px;background:var(--white)}
.brand{left:83px;top:56px;display:flex;align-items:center;gap:8px}
.brand-mark{width:24px;height:24px;background:var(--blue)}
.brand-name{font-size:20px;font-weight:400;color:var(--ink)}
.nav{top:63px;left:0;font-size:12px;color:var(--ink)}
.nav span{position:absolute;white-space:nowrap}
.hero{left:0;top:104px;width:1125px;height:444px;
  background:radial-gradient(ellipse at 78% 18%,rgba(170,60,160,.55),transparent 30%),
  radial-gradient(ellipse at 30% 35%,#6b7784 0%,#3a424a 35%,transparent 60%),
  linear-gradient(160deg,#2b3036 0%,#3b3532 55%,#1d1b1a 100%)}
.hero-title{left:0;width:1125px;top:268px;text-align:center;font-size:33px;font-weight:300;color:var(--white)}
.hero-title em{font-style:normal;font-weight:400;color:var(--blue)}
.hero-text{left:0;width:1125px;top:320px;text-align:center;font-size:14px;line-height:19.5px;color:var(--white)}
.why{left:0;top:548px;width:563px;height:261px;background:var(--blue);color:var(--white)}
.join{left:563px;top:548px;width:562px;height:261px;background:var(--panel)}
.section-title{font-size:26px;font-weight:300}
.why-list li{position:absolute;list-style:none;font-size:12px;display:flex;align-items:center;gap:8px;white-space:nowrap}
.field{height:38px;background:var(--field);display:flex;align-items:center;font-size:12px;color:#444}
.field .ic{width:35px;display:flex;justify-content:center;border-right:1px solid #ccc;height:20px;align-items:center;margin-right:10px}
.submit{background:var(--orange);color:var(--white);font-size:12px;display:flex;align-items:center;justify-content:center}
.agree{font-size:12px;color:#444;display:flex;align-items:center;gap:15px}
.agree .box{width:15px;height:14px;border:1px solid #333;background:var(--white)}
.frame{left:69px;top:847px;width:273px;height:220px;border:2.5px solid var(--orange);border-right-width:2.5px}
.offer-photo{left:83px;top:863px;width:355px;height:237px;background:linear-gradient(120deg,#c9b27a 0%,#8a7a56 35%,#2f5e96 65%,#23487a 100%)}
.offer-title{left:489px;top:899px;font-size:33px;font-weight:300;color:var(--ink)}
.offer-title em{font-style:normal;color:var(--blue)}
.offer-text{left:489px;top:952px;width:555px;font-size:14px;line-height:23.4px;color:#333}
.offer-text p+p{margin-top:8px}
.footer{left:0;top:1152px;width:1125px;height:48px;background:var(--dark);color:var(--white);font-size:12px}
</style>
</head>
<body>
<div class="abs topbar"></div>
<div class="abs social one"></div>
<div class="abs social two"></div>
<div class="abs social three"></div>
<div class="abs account" style="left:925px"><span class="signin">Sign in</span><span class="sep">|</span>Register</div>

<div class="abs header"></div>
<div class="abs brand"><span class="brand-mark"></span><span class="brand-name">Bramwelloq</span></div>
<div class="abs nav">
  <span style="left:571px;top:-2px"><svg width="17" height="15" viewBox="0 0 17 15"><path d="M8.5 0L0 7.5h2.5V15h4.2v-5h3.6v5h4.2V7.5H17z" fill="var(--blue)"/></svg></span>
  <span style="left:607px">About Our School</span>
  <span style="left:729px">Risk Warning</span>
  <span style="left:828px">FAQ</span>
  <span style="left:881px">Trading Glossary</span>
  <span style="left:1001px">Contact</span>
</div>

<div class="abs hero" role="img" aria-label="Photo of hands typing on a laptop showing a blog editor, dimmed"></div>
<h1 class="abs hero-title" style="font-weight:300">Online Trading <em>School</em></h1>
<p class="abs hero-text">Lorem ipsum dolor sit amet, consectetuer adipiscing elit aenean commodo ligula<br>penatibus et magnis dis parturient montes nascetur ridiculus.</p>

<section class="abs why">
  <h2 class="abs section-title" style="left:83px;top:61px">Why To Join Us</h2>
  <ul class="why-list">
    <li style="left:82px;top:106px"><svg width="16" height="16" viewBox="0 0 16 16"><circle cx="8" cy="8" r="8" fill="#fff"/><path d="M4.5 8.2l2.3 2.3 4.7-4.7" stroke="var(--blue)" stroke-width="1.8" fill="none"/></svg>Best trading tips ever</li>
    <li style="left:82px;top:138px"><svg width="16" height="16" viewBox="0 0 16 16"><circle cx="8" cy="8" r="8" fill="#fff"/><path d="M4.5 8.2l2.3 2.3 4.7-4.7" stroke="var(--blue)" stroke-width="1.8" fill="none"/></svg>Secrect tips from experts</li>
    <li style="left:82px;top:167px"><svg width="16" height="16" viewBox="0 0 16 16"><circle cx="8" cy="8" r="8" fill="#fff"/><path d="M4.5 8.2l2.3 2.3 4.7-4.7" stroke="var(--blue)" stroke-width="1.8" fill="none"/></svg>We teach you how to trade online</li>
    <li style="left:302px;top:106px"><svg width="16" height="16" viewBox="0 0 16 16"><circle cx="8" cy="8" r="8" fill="#fff"/><path d="M4.5 8.2l2.3 2.3 4.7-4.7" stroke="var(--blue)" stroke-width="1.8" fill="none"/></svg>Learn how to trade commoditites</li>
    <li style="left:302px;top:138px"><svg width="16" height="16" viewBox="0 0 16 16"><circle cx="8" cy="8" r="8" fill="#fff"/><path d="M4.5 8.2l2.3 2.3 4.7-4.7" stroke="var(--blue)" stroke-width="1.8" fill="none"/></svg>Learn how to become a trader</li>
  </ul>
</section>

<section class="abs join">
  <h2 class="abs section-title" style="left:54px;top:61px;color:var(--ink)">Join Our School Now !</h2>
  <div class="abs field" style="left:54px;top:104px;width:211px"><span class="ic"><svg width="10" height="12" viewBox="0 0 10 12"><circle cx="5" cy="3" r="3" fill="#888"/><path d="M0 12c0-4 2-5.5 5-5.5s5 1.5 5 5.5z" fill="#888"/></svg></span>First Name</div>
  <div class="abs field" style="left:269px;top:104px;width:211px"><span class="ic"><svg width="10" height="12" viewBox="0 0 10 12"><circle cx="5" cy="3" r="3" fill="#888"/><path d="M0 12c0-4 2-5.5 5-5.5s5 1.5 5 5.5z" fill="#888"/></svg></span>Last Name</div>
  <div class="abs field" style="left:54px;top:146px;width:211px;height:37px"><span class="ic"><svg width="12" height="9" viewBox="0 0 12 9"><rect width="12" height="9" fill="#888"/><path d="M0 0l6 5 6-5" stroke="#e6e6e6" fill="none"/></svg></span>Email Name</div>
  <div class="abs submit" style="left:269px;top:146px;width:211px;height:37px">SUBMIT</div>
  <div class="abs agree" style="left:55px;top:194px"><span class="box"></span>Agree with our terms and conditions</div>
</section>

<div class="abs frame"></div>
<div class="abs offer-photo" role="img" aria-label="Photo of a person in a denim shirt working at a laptop with a phone on a café table"></div>
<h2 class="abs offer-title">What We <em>Offer</em></h2>
<div class="abs offer-text">
  <p>Lorem ipsum dolor sit amet, consectetuer adipiscing elit. Aenean commodo ligula eget dolor. Aenean massa. Cum sociis natoque penatibus et magnis dis parturient montes, nascetur ridiculus mus. Donec quam felis, ultricies nec</p>
  <p>Donec quam felis, ultricies nec, pellentesque eu, pretium quis, sem. Nulla consequat massa quis enim. Donec pede justo, fringilla vel, aliquet nec .</p>
</div>

<footer class="abs footer">
  <span class="abs" style="left:83px;top:19px">Copyright 2016 | All Right Reserved</span>
  <span class="abs" style="left:855px;top:18px">Terms &amp; Conditions | Privacy Policy</span>
</footer>
</body>
</html>
```